Powerpoint Presentation Template

Kindly design a business class Powepoint Presentation template for our business use. Please stick to our company colours or even pictures as shown on our website and Logo

```html
<!DOCTYPE html>
<html lang="en">
<head>
<meta charset="utf-8">
<title>Presentation Slide Template</title>
<link rel="stylesheet" href="https://fonts.googleapis.com/css2?family=Carlito:wght@400&display=swap">
<style>
  :root {
    --stage: #000000;
    --slide: #ffffff;
    --brand: #a5493a;
    --brand-dark: #7a2f22;
    --brand-light: #a8483a;
    --ink: #000000;
  }
  html, body {
    margin: 0;
    padding: 0;
    width: 1200px;
    height: 750px;
    overflow: hidden;
    background: var(--stage);
  }
  .slide {
    position: absolute;
    left: 0;
    top: 37.5px;
    width: 1200px;
    height: 675px;
    background: var(--slide);
    overflow: hidden;
    font-family: "Carlito", "Calibri", sans-serif;
  }
  .slide-wave {
    position: absolute;
    inset: 0;
    width: 100%;
    height: 100%;
  }
  .slide-title {
    position: absolute;
    left: 91px;
    top: 66px;
    margin: 0;
    font-size: 50px;
    font-weight: 400;
    line-height: 1;
    color: var(--brand);
  }
  .slide-body {
    position: absolute;
    left: 91px;
    top: 182px;
    margin: 0;
    padding: 0;
    list-style: none;
    font-size: 30px;
    line-height: 1.2;
    color: var(--ink);
  }
  .slide-body li {
    position: relative;
    padding-left: 22px;
  }
  .slide-body li::before {
    content: "";
    position: absolute;
    left: 1px;
    top: 14px;
    width: 8px;
    height: 8px;
    border-radius: 50%;
    background: var(--ink);
  }
  .brand-name {
    position: absolute;
    right: 15px;
    top: 36px;
    text-align: right;
    color: var(--brand-dark);
    font-size: 17px;
    font-weight: 400;
    line-height: 1.05;
    letter-spacing: 0.5px;
  }
</style>
</head>
<body>
  <section class="slide">
    <svg class="slide-wave" viewBox="0 0 1440 810" preserveAspectRatio="none" aria-hidden="true">
      <defs>
        <linearGradient id="waveFill" x1="0" y1="0" x2="0" y2="1">
          <stop offset="0" stop-color="var(--brand-dark)" style="stop-color:#7a2f22"/>
          <stop offset="1" stop-color="var(--brand-light)" style="stop-color:#a8483a"/>
        </linearGradient>
      </defs>
      <path d="M0,370 C40,520 300,780 930,808 C1150,812 1320,768 1440,725 L1440,810 L0,810 Z" fill="url(#waveFill)"/>
    </svg>

    <div class="brand-name">KESTREL<br>Properties</div>

    <h1 class="slide-title">Header</h1>
    <ul class="slide-body">
      <li>Text</li>
    </ul>
  </section>
</body>
</html>
```